I have a business that exists already (Belvina Conservatory of Music) that we offer music lessons to all instruments. I recently opened a smaller version called TONES by Belvina that will only teach piano lessons. What I'm looking for now is a 3 page Website on word press. After I choose the design I like I want to be able to take over the website and bring it to our hosting company. We want full control of it and our team will take over. The reason I'm doing this is to have other visions and ideas from others. The first page will be about the company and our message/vision. Second page about the piano lessons. The third will be about franchising this concept "Tones by Belvina" Attached are 3 Logos . Please refer to our existing website www.belvinamusicschool-example.com to look at our piano page and franchising page. Please feel free to message me if you need more info. Thanks
Please note I do not want the new website (Tones by Belvina) To look like the other Website (Belvina Conservatory of Music) Fresh new look. I do not want the colours red or using the Red logo. I only provided it so that you have an Idea of What the other business looks like and that you can take the piano content and franchise content off of it. Tones by Belvina is smaller concept and only piano lessons.
Thanks
Only Piano lessons for all students
3 page

```html
<!DOCTYPE html>
<html lang="en">
<head>
<meta charset="utf-8">
<title>TONES by Belvina – Piano Lessons</title>
<link rel="stylesheet" href="https://fonts.googleapis.com/css2?family=Libre+Baskerville:ital@0;1&family=Mulish:wght@400;600;700&family=Dancing+Script:wght@600&display=swap">
<style>
:root{
  --black:#000;
  --white:#fff;
  --orange:#f08a31;
  --orange-soft:#f7c9a1;
  --grey-bg:#f4f3f2;
  --cream:#fdf4ee;
  --text:#1b1b1b;
  --muted:#4a4a4a;
  --line:#c9c9c9;
}
*{box-sizing:border-box;margin:0;padding:0}
html,body{width:1200px;height:3544px;overflow:hidden;background:var(--white)}
body{position:relative;font-family:"Mulish",sans-serif;color:var(--text)}
.abs{position:absolute}
.serif{font-family:"Libre Baskerville",serif}
.btn{position:absolute;display:flex;align-items:center;justify-content:center;background:var(--orange);color:var(--white);border-radius:20px;font-family:"Dancing Script",cursive;font-size:19px;text-decoration:none}
.photo{position:absolute}

/* hero */
.hero{position:absolute;left:0;top:0;width:1200px;height:983px;background:var(--black)}
.hero-photo{left:0;top:0;width:690px;height:590px;background:radial-gradient(ellipse at 35% 40%,#8a6a4c 0%,#4a3526 35%,#1a120c 65%,#000 100%)}
.brand{position:absolute;left:145px;top:28px;color:var(--white);font-family:"Libre Baskerville",serif;font-size:30px;letter-spacing:1px}
.brand small{font-size:17px;letter-spacing:0}
.nav{position:absolute;top:47px;left:0;width:1200px;font-family:"Libre Baskerville",serif;font-size:14px;color:var(--white)}
.nav a{position:absolute;color:var(--white);text-decoration:none}
.nav a.active{color:var(--orange)}
.hero-lead{left:775px;top:218px;color:var(--white);font-size:22px}
.hero-title{left:773px;top:246px;color:var(--orange);font-size:47px;font-family:"Libre Baskerville",serif}
.hero-sub{left:775px;top:300px;color:var(--white);font-size:32px;font-family:"Libre Baskerville",serif}
.section-title{font-family:"Libre Baskerville",serif;font-size:31px;text-transform:uppercase}
.body-copy p{font-size:13px;line-height:21.6px;margin-bottom:7px;letter-spacing:.3px}
.playing{left:145px;top:606px;width:485px;color:var(--white)}
.playing h2{margin-bottom:20px}
.kid-photo{left:663px;top:495px;width:395px;height:541px;background:linear-gradient(160deg,#6b5a48 0%,#a07d58 45%,#3c2d22 100%)}

/* vision */
.vision-back{left:0;top:1036px;width:325px;height:288px;background:linear-gradient(135deg,#3b3430,#7a6a5c)}
.vision-photo{left:106px;top:1135px;width:428px;height:410px;background:linear-gradient(135deg,#d9d9d6 0%,#9fb0c2 45%,#f2f2f0 100%)}
.vision{left:578px;top:1190px;width:482px}
.vision h2{margin-bottom:20px}

/* programs */
.programs{position:absolute;left:0;top:1632px;width:1200px;height:865px;background:var(--grey-bg)}
.prog-head{left:142px;top:1792px}
.prog-head h3{font-family:"Libre Baskerville",serif;font-size:20px;font-weight:400;line-height:27px;margin-top:6px}
.frame-right{left:897px;top:1717px;width:161px;height:317px;background:var(--orange)}
.prog-photo{left:575px;top:1739px;width:462px;height:342px;background:linear-gradient(135deg,#7b6a58 0%,#2f2a26 55%,#111 100%)}
.frame-left{left:142px;top:2025px;width:161px;height:317px;background:var(--orange)}
.prog-photo2{left:162px;top:1980px;width:284px;height:341px;background:linear-gradient(120deg,#c9a27b 0%,#fbe9d2 50%,#8d6a4c 100%)}
.prog-list{left:603px;top:2124px;width:440px;list-style:none}
.prog-list li{font-size:13.5px;line-height:19.5px;margin-bottom:10.5px}
.keys-band{left:0;top:2497px;width:1200px;height:118px;background:linear-gradient(180deg,#e4e4e4,#cfcfcf 70%,#f2f2f2)}

/* quote */
.quote-mark{font-family:"Libre Baskerville",serif;color:var(--orange-soft);font-size:96px;line-height:1}
.quote{left:250px;top:2733px;width:700px;text-align:center;font-family:"Libre Baskerville",serif;font-style:italic;font-size:18px}
.quote-rule{left:435px;top:2807px;width:329px;height:1px;background:var(--line)}
.quote-name{left:0;top:2833px;width:1200px;text-align:center;font-family:"Libre Baskerville",serif;font-size:16px}
.stars{left:0;top:2855px;width:1200px;text-align:center;color:var(--orange);font-size:14px;letter-spacing:1px}

/* franchise */
.franchise{left:263px;top:2954px;width:680px;height:216px;background:var(--cream);text-align:center}
.franchise h2{font-family:"Libre Baskerville",serif;font-weight:400;font-size:31px;margin-top:48px}
.franchise p{font-size:17px;color:var(--muted);margin-top:10px}

/* footer */
.footer{position:absolute;left:0;top:3256px;width:1200px;height:249px;background:var(--black);color:var(--white)}
.footer h4{font-family:"Libre Baskerville",serif;font-weight:400;font-size:12px;position:absolute;top:56px}
.quick{position:absolute;left:142px;top:83px;list-style:none;font-size:12.5px}
.quick li{margin-bottom:9px}
.quick li::before{content:"» ";margin-right:6px}
.contact{position:absolute;left:337px;top:83px;font-size:12.5px;line-height:17px}
.contact .row{display:flex;gap:8px;margin-bottom:12px}
.contact svg{flex:none;margin-top:2px}
.map{position:absolute;left:622px;top:78px;width:209px;height:124px;border:3px solid #bbb;background:linear-gradient(120deg,#bcd7ef 0%,#e9eef0 40%,#f4f1ea 100%)}
.foot-brand{position:absolute;left:922px;top:90px;font-family:"Libre Baskerville",serif;font-size:26px;color:var(--white)}
.foot-brand small{font-size:15px}
.social{position:absolute;top:170px;width:24px;height:24px;border-radius:50%;background:var(--orange)}
.copyright{position:absolute;left:0;top:3505px;width:1200px;height:39px;background:var(--orange);color:var(--white);font-size:11.5px;display:flex;align-items:center;justify-content:center}
</style>
</head>
<body>

<section class="hero">
  <div class="photo hero-photo" role="img" aria-label="Young woman playing a grand piano on a dimly lit stage"></div>
  <div class="brand">TONES <small>by Belvina</small></div>
  <nav class="nav">
    <a class="active" style="left:593px">HOME</a>
    <a style="left:676px">PIANO LESSONS</a>
    <a style="left:826px">FRANCHISING</a>
    <a style="left:963px">CONTACT US</a>
  </nav>
  <div class="abs hero-lead">We Will Provide</div>
  <div class="abs hero-title">Piano Lessons</div>
  <div class="abs hero-sub">For All Students</div>
  <a class="btn" style="left:775px;top:355px;width:168px;height:37px">Contact Us Today</a>

  <div class="abs playing body-copy">
    <h2 class="section-title" style="font-weight:400">Playing the Piano</h2>
    <p>When you think of a piano, you probably envision black and white keys but the piano is more than those harmonious sounds created by the player.</p>
    <p>The versatility and the musicianship instilled into the player from those keys is the true magic that comes from playing piano! Starting from the grassroots, experience different methods and styles of playing piano. To mark the milestones of progression, engage in one of Belvina's many unique performance opportunities like annual festival competitions, recitals or our examinations (Belvina &amp; HMC).</p>
  </div>
  <a class="btn" style="left:145px;top:860px;width:139px;height:36px">Read More</a>
</section>
<div class="photo kid-photo" role="img" aria-label="Little girl in a polka dot top practising at the piano"></div>

<div class="photo vision-back" role="img" aria-label="Close view of hands on piano keys"></div>
<div class="photo vision-photo" role="img" aria-label="Teacher and boy playing a white piano together"></div>
<div class="abs vision body-copy">
  <h2 class="section-title" style="font-weight:400">Our Vision</h2>
  <p>Lorem ipsum dolor sit amet, consectetuer adipiscing elit, sed diam nonummy nibh euismod tincidunt ut laoreet dolore magna aliquam erat</p>
  <p>Lorem ipsum dolor sit amet, consectetuer adipiscing elit, sed diam nonummy nibh euismod tincidunt ut laoreet dolore magna aliquam erat volutpat. Ut wisi enim ad minim veniam, quis nostrud exerci tation ullamcorper suscipit lobortis nisl ut aliquip ex ea commodo consequat. Duis autem vel eum iriure dolor in hendrerit in vulputate velit esse molestie consequat, vel illum dolore eu feugiat nulla facilisis at vero eros et .</p>
</div>
<a class="btn" style="left:578px;top:1443px;width:168px;height:39px">Contact Us Today</a>

<section class="programs"></section>
<div class="abs prog-head">
  <h2 class="section-title" style="font-weight:400">Our Programs</h2>
  <h3>ALSO PROVIDE STUDENTS THE<br>OPPORTUNITY TO</h3>
</div>
<div class="abs frame-right"></div>
<div class="photo prog-photo" role="img" aria-label="Smiling girl seated at a black grand piano"></div>
<div class="abs frame-left"></div>
<div class="photo prog-photo2" role="img" aria-label="Child's hands on piano keys in warm sunlight"></div>
<ul class="abs prog-list">
  <li>Participate in large-scale performances.</li>
  <li>Perform at Belvina's many community events on a regular basis.</li>
  <li>Access the GTA's coolest Broadcast stage</li>
  <li>Attend Clinics, Masterclasses, and Jam Nights</li>
  <li>Access the Belvina Rocks band program. Belvina's Band Program empowers and electrifies students to come together, create music and confidently hit the stage with their own band identity while having fun and honing their instrument.</li>
  <li>Register in our elite teaching program to learn how to pass on the magic and passion of playing the piano to students.</li>
</ul>
<a class="btn" style="left:603px;top:2396px;width:168px;height:38px">Contact Us Today</a>
<div class="abs keys-band" role="img" aria-label="Decorative band of piano keys"></div>

<div class="abs quote-mark" style="left:244px;top:2690px">&ldquo;</div>
<div class="abs quote-mark" style="left:880px;top:2750px">&rdquo;</div>
<p class="abs quote">Life is like a piano. What you get out of it depends on how you play it.</p>
<div class="abs quote-rule"></div>
<svg class="abs" style="left:593px;top:2806px" width="14" height="8" viewBox="0 0 14 8"><path d="M0 0 L7 7 L14 0 Z" fill="#c9c9c9"/></svg>
<div class="abs quote-name">THEO LARKIN</div>
<div class="abs stars">☆☆☆☆☆</div>

<div class="abs franchise">
  <h2>Franchise Opportunities</h2>
  <p>Be part of the Belvina academy family</p>
</div>
<a class="btn" style="left:537px;top:3084px;width:132px;height:38px">Know More</a>

<footer class="footer">
  <h4 style="left:142px">QUICK LINKS</h4>
  <ul class="quick">
    <li>Home</li><li>Piano Lessons</li><li>Franchising</li><li>Contact Us</li>
  </ul>
  <h4 style="left:337px">CONTACT DETAILS</h4>
  <div class="contact">
    <div class="row">
      <svg width="12" height="14" viewBox="0 0 12 14"><path d="M6 0a5 5 0 0 0-5 5c0 4 5 9 5 9s5-5 5-9a5 5 0 0 0-5-5zm0 7a2 2 0 1 1 0-4 2 2 0 0 1 0 4z" fill="#fff"/></svg>
      <div><b style="font-size:11px">Tones by Belvina</b><br>123 ipsum dolor sit amet,<br>consectetuer adipiscing.</div>
    </div>
    <div class="row">
      <svg width="13" height="13" viewBox="0 0 24 24"><path d="M6.6 10.8a15 15 0 0 0 6.6 6.6l2.2-2.2c.3-.3.7-.4 1-.2 1.1.4 2.3.6 3.6.6.6 0 1 .4 1 1V20c0 .6-.4 1-1 1A17 17 0 0 1 3 4c0-.6.4-1 1-1h3.5c.6 0 1 .4 1 1 0 1.3.2 2.5.6 3.6.1.3 0 .7-.2 1z" fill="#fff"/></svg>
      <div>1-800-555-0147</div>
    </div>
    <div class="row">
      <svg width="13" height="11" viewBox="0 0 13 11"><rect x=".5" y=".5" width="12" height="10" fill="none" stroke="#fff"/><path d="M.5 .5 L6.5 6 L12.5 .5" fill="none" stroke="#fff"/></svg>
      <div>info@tonesbybelvina-example.com</div>
    </div>
  </div>
  <h4 style="left:622px">LOCATION MAP</h4>
  <div class="map" role="img" aria-label="Location map of the school area"></div>
  <div class="foot-brand">TONES <small>by Belvina</small></div>
  <span class="social" style="left:929px"></span>
  <span class="social" style="left:959px"></span>
  <span class="social" style="left:990px"></span>
  <span class="social" style="left:1021px"></span>
</footer>
<div class="copyright">Copyright © 2020&nbsp;<b>Tones by Belvina</b>. All Rights Reserved.</div>

</body>
</html>
```